Civil Engineering Web design

.Net Web design for a civil engineering company to include a blog page, I will like a site similar to this http://www.layoutgrove.example/demo/58273.html

company name: Dorvil Associates

-Civil/Structural Engineering Solutions

-Engineering Design Development and Consultancy

More Information about the internal pages or links:
1. Each one of the menu choices will take you to a page for that option where I will be able to insert text 2. Our team likewise should be a page with space for a photo of the staff and text space for inserting employee name and title, qualifications and job description and work experience...
Can we have 3 groups for these
Management Staff
Support Staff
Other Staff

3. The blog is a generic blog page where users can add comments to a any subjects raised by our team and submit... When they submit, the comments should be emailed to us 4. Contact us is also a tool for emailing us by users, whereby they provide their email, subject and email body 5. projects is a page that allows insertion of title, one photo and description of the project...
6. services is a page with links on the left for Construction Supervision Civil and Structured Engineering Designs Corporate Recognition

Each on when clicked should display the relevant information for the link which is a gallery of two photos side by side and one description per pair...

Industry/Entity Type

Construction

Requirements
Must have
• User ability to manage content; not design

Pages:
Home
Services
Projects (sub page picture gallery)
Reference
Our Team
Blog
Contact Us

```html
<!DOCTYPE html>
<html lang="en">
<head>
<meta charset="utf-8">
<title>Dorvil Associates</title>
<link href="https://fonts.googleapis.com/css2?family=Open+Sans:wght@300;400;700&display=swap" rel="stylesheet">
<style>
:root{
  --yellow:#f8b500;
  --yellow-light:#ffd84a;
  --ink:#111111;
  --menu-text:#5a5a5a;
  --menu-line:#3b4a5a;
  --white:#ffffff;
  --ribbon:#1f4c56;
  --footer-text:#6f6f6f;
}
*{margin:0;padding:0;box-sizing:border-box}
html,body{width:1200px;height:834px;overflow:hidden;background:var(--white);font-family:"Open Sans",sans-serif}
.page{position:relative;width:1200px;height:834px}
.hero-photo{position:absolute;left:0;top:0;width:1200px;height:790px;
  background:linear-gradient(180deg,#2f8d9a 0%,#3f90a0 22%,#7f7f86 38%,#b4653a 48%,#8d7a6e 60%,#8c8c90 80%,#7d7f84 100%)}
.sidebar{position:absolute;left:120px;top:0;width:197px}
.brand{height:136px;background:linear-gradient(180deg,#ffffff 70%,#e6e6e6 100%);padding:40px 0 0 16px}
.brand-name{font-size:27px;font-weight:700;color:var(--ink);line-height:30px}
.menu{list-style:none}
.menu li{height:32px;line-height:32px;padding-left:17px;font-size:16px;color:var(--menu-text);
  background:linear-gradient(180deg,#ffffff,#ececec);border-bottom:1px solid var(--menu-line)}
.menu li.active{background:linear-gradient(180deg,var(--yellow-light),var(--yellow));color:var(--white)}
.menu-foot{display:block}
.headline{position:absolute;left:489px;top:184px;width:490px;color:var(--white);
  font-weight:300;font-size:44px;line-height:46px;letter-spacing:-.6px}
.rule{position:absolute;left:494px;top:354px;width:32px;height:5px;border-top:1px solid var(--yellow);border-bottom:1px solid var(--yellow)}
.cta{position:absolute;left:495px;top:405px;width:178px;height:45px;border:1px solid var(--yellow);
  color:var(--yellow);font-weight:700;font-size:23px;line-height:43px;text-align:center}
.or{position:absolute;left:694px;top:413px;width:28px;height:28px;border-radius:50%;
  background:rgba(80,80,80,.75);color:var(--white);font-size:11px;line-height:28px;text-align:center}
.learn{position:absolute;left:739px;top:415px;color:var(--white);font-size:16px}
.slide-next{position:absolute;left:987px;top:476px}
.social{position:absolute;left:1045px;top:0}
.footer{position:absolute;right:118px;top:800px;font-size:11.5px;color:var(--footer-text)}
</style>
</head>
<body>
<div class="page">
  <div class="hero-photo" role="img" aria-label="Engineer's desk with tablet, calculator, pens and hard hats in front of a construction site with cranes"></div>

  <aside class="sidebar">
    <div class="brand">
      <div class="brand-name">Dorvil<br>Associates</div>
    </div>
    <ul class="menu">
      <li class="active">Home</li>
      <li>Services</li>
      <li>Projects</li>
      <li>Reference</li>
      <li>Our Team</li>
      <li>Blog</li>
      <li>Contact Us</li>
    </ul>
    <svg class="menu-foot" width="197" height="52" viewBox="0 0 197 52">
      <defs><linearGradient id="wedge" x1="0" y1="0" x2="0" y2="1"><stop offset="0" stop-color="#ffd84a"/><stop offset="1" stop-color="#f8b500"/></linearGradient></defs>
      <polygon points="0,0 197,0 0,52" fill="url(#wedge)"/>
      <circle cx="24" cy="19" r="7" fill="#333"/>
      <rect x="20" y="18" width="8" height="2" fill="#f8b500"/>
    </svg>
  </aside>

  <h1 class="headline">Civil Engineering is a Research and Development Company</h1>
  <div class="rule"></div>
  <div class="cta">Call to Action</div>
  <div class="or">or</div>
  <div class="learn">Learn More &#187;</div>

  <svg class="slide-next" width="54" height="54" viewBox="0 0 54 54">
    <circle cx="27" cy="27" r="25" fill="none" stroke="rgba(255,255,255,.35)" stroke-width="1.5"/>
    <polyline points="23,18 32,27 23,36" fill="none" stroke="rgba(255,255,255,.4)" stroke-width="1.5"/>
  </svg>

  <svg class="social" width="37" height="114" viewBox="0 0 37 114">
    <polygon points="0,0 37,0 37,114 18.5,104 0,114" fill="var(--ribbon)" opacity=".9"/>
    <circle cx="18.5" cy="22" r="11" fill="none" stroke="#ffffff" stroke-width="1.5"/>
    <circle cx="18.5" cy="52" r="11" fill="none" stroke="#ffffff" stroke-width="1.5" opacity=".7"/>
    <circle cx="18.5" cy="81" r="11" fill="none" stroke="#ffffff" stroke-width="1.5" opacity=".7"/>
  </svg>

  <footer class="footer">&copy; Copyright 2014 - www.civilworks.example &nbsp;- &nbsp;Help &nbsp;- Terms</footer>
</div>
</body>
</html>
```